Business Card Design

We need a business card design for a new business based in Sutton, NH called 'Fern Ridge Repair'. We service home standby generators as well as other power equipment such as chainsaws, snowblowers and mowers. Our target audience is residential customers-hence the Fern Ridge slogan. "Fern Ridge Repair..." We would like to see designs that include a roof line and wrenches that would communicate this type of service. We would like to see designs that use the colors of orange, tan and dark green. The final design should communicate strong, reliable service....please incorporate a small Christian fish emblem somewhere in the design.

Target Market(s)

Residents who have standby generators and power equipment

Industry/Entity Type

Residential

Contact Information for Business Card

Fern Ridge Repair, Dale Whitfield, 517 Maple Crest Rd, Alder Glen NH 03498, 603-555-0182 Cell: 603-555-0147

```html
<!DOCTYPE html>
<html lang="en">
<head>
<meta charset="utf-8">
<title>Fern Ridge Repair — Business Card</title>
<link rel="stylesheet" href="https://fonts.googleapis.com/css2?family=Roboto+Condensed:wght@400;700&display=swap">
<style>
  :root {
    --green: #168356;
    --orange: #f26f2a;
    --white: #ffffff;
    --stage: #e9e7e3;
    --card-radius: 30px;
  }
  * { box-sizing: border-box; margin: 0; padding: 0; }
  html, body {
    width: 1200px; height: 855px; overflow: hidden;
    background: var(--stage);
    font-family: "Roboto Condensed", "Arial Narrow", sans-serif;
  }
  .stage {
    width: 1200px; height: 855px;
    display: flex; align-items: center; justify-content: center; gap: 40px;
  }
  .card {
    position: relative;
    width: 540px; height: 310px;
    background: var(--white);
    border-radius: var(--card-radius);
    overflow: hidden;
    box-shadow: 0 14px 30px rgba(0,0,0,.18);
  }

  /* shared wordmark */
  .wordmark { display: flex; align-items: center; gap: 14px; }
  .wordmark__square { width: 34px; height: 34px; background: var(--orange); flex: none; }
  .wordmark__name {
    color: var(--green); font-weight: 700; text-transform: uppercase;
    line-height: .92; letter-spacing: .5px;
  }

  /* front */
  .card--front .wordmark { position: absolute; left: 150px; top: 78px; }
  .card--front .wordmark__square { width: 44px; height: 44px; }
  .card--front .wordmark__name { font-size: 46px; }
  .front-band {
    position: absolute; left: 0; right: 0; bottom: 0; height: 62px;
    background: var(--green);
    border-top: 6px solid var(--orange);
    box-shadow: 0 -5px 0 var(--white);
    display: flex; align-items: center; padding-left: 70px;
  }
  .front-band__address {
    color: var(--white); font-size: 22px; text-transform: uppercase; letter-spacing: .3px;
    white-space: nowrap;
  }

  /* back */
  .card--back .wordmark { position: absolute; left: 40px; top: 36px; }
  .card--back .wordmark__name { font-size: 30px; }
  .contact { position: absolute; left: 40px; top: 150px; }
  .contact__name {
    color: var(--green); font-weight: 700; font-size: 24px; text-transform: uppercase; margin-bottom: 10px;
  }
  .contact__phones { display: flex; align-items: flex-start; gap: 10px; }
  .contact__icon { width: 22px; height: 22px; margin-top: 1px; }
  .contact__numbers { color: var(--green); font-size: 19px; line-height: 1.25; }
  .back-panel { position: absolute; inset: 0; width: 100%; height: 100%; }
  .services {
    position: absolute; right: 46px; top: 62px;
    text-align: right; color: var(--white); font-size: 21px; line-height: 1.55;
    list-style: none;
  }
  .services__title { font-weight: 700; }
</style>
</head>
<body>
<main class="stage">
  <section class="card card--front" aria-label="Card front">
    <div class="wordmark">
      <span class="wordmark__square"></span>
      <span class="wordmark__name">Fern Ridge<br>Repair</span>
    </div>
    <div class="front-band">
      <p class="front-band__address">517 Maple Crest Rd, Alder Glen NH 03498,</p>
    </div>
  </section>

  <section class="card card--back" aria-label="Card back">
    <svg class="back-panel" viewBox="0 0 540 310" preserveAspectRatio="none" aria-hidden="true">
      <polygon points="316,0 274,155 316,310 300,310 258,155 300,0" fill="var(--orange)"/>
      <polygon points="326,0 540,0 540,310 326,310 284,155" fill="var(--green)"/>
    </svg>
    <div class="wordmark">
      <span class="wordmark__square"></span>
      <span class="wordmark__name">Fern Ridge<br>Repair</span>
    </div>
    <div class="contact">
      <p class="contact__name">Dale Whitfield</p>
      <div class="contact__phones">
        <svg class="contact__icon" viewBox="0 0 24 24" aria-hidden="true">
          <circle cx="12" cy="12" r="12" fill="var(--orange)"/>
          <path d="M8.2 6.5l2 2.2-1 1.5c.8 1.7 2 2.9 3.6 3.7l1.5-1 2.2 2-1.2 2c-4.6-.4-8.3-4.1-8.7-8.7z" fill="var(--white)"/>
        </svg>
        <p class="contact__numbers">603-555-0182<br>603-555-0147</p>
      </div>
    </div>
    <ul class="services">
      <li class="services__title">We service</li>
      <li>Generators</li>
      <li>Chainsaws</li>
      <li>Snowblowers</li>
      <li>and Mowers</li>
    </ul>
  </section>
</main>
</body>
</html>
```